Looking for new banner ad to use in online magazine advertisements

We are looking for design ideas for a few ads we need to publish in online magazines. We are a plumbing distributor that specializes in backflow repair parts. Our web page is www.drainkitdepot.com which shows the products and manufacturers we sell. We are looking for an ad that can be displayed in a few different size formats so please send over your ideas for each size listed below.
We are redesigning our website and we have a test site up were you can get a look at the design we are going with as well as pull photos and images from. The web addresss for our new site is http://pipeline.stagehollow.com/

We need to have an ad that is 600 x 100, 120 x 500, and a half page ad that would be 600 x 200

I have attached a few of the print flyers we are using at this point so you can have an idea of past designs we have gone with.

Industry/Entity Type

Distribution

Requirements
Must have
• We need to have an ad that is 600 x 100, 120 x 500, and a half page ad that would be 600 x 200
• 600 w x 100 h
• 120 w x 500 h
• 600 w x 200 h
Nice to have
• See webpages below for images and design ideas.
• Old website: www.drainkitdepot.com
• New web page: http://pipeline.stagehollow.com/

```html
<!DOCTYPE html>
<html lang="en">
<head>
<meta charset="utf-8">
<title>Crestline Valve Supply – Banner Set</title>
<link rel="stylesheet" href="https://fonts.googleapis.com/css2?family=Arimo:ital,wght@0,400;0,700;1,700&display=swap">
<style>
  :root{
    --brand-red:#d0174a;
    --cta-red:#c0143c;
    --ink:#111111;
    --navy:#3d4170;
    --frame:#bdbdbd;
    --board-top:#ffffff;
    --board-bottom:#e6e6e6;
    --gauge-dark:#1e2326;
    --gauge-face:#e9ece8;
  }
  *{box-sizing:border-box;margin:0;padding:0}
  html,body{width:1200px;height:660px;overflow:hidden;background:var(--board-top)}
  .canvas{width:1200px;height:660px;overflow:hidden;position:relative;
    background:linear-gradient(180deg,var(--board-top) 0%,var(--board-top) 35%,var(--board-bottom) 100%)}
  .stage{position:absolute;left:0;top:0;width:1296px;height:713px;transform:scale(0.9259);transform-origin:0 0;
    font-family:"Arimo",Arial,sans-serif;color:var(--ink)}

  .submission-notes{position:absolute;left:45px;top:219px;font-size:16px;line-height:26px;color:var(--ink)}
  .submission-notes strong{font-weight:700}

  .banner{position:absolute;background:#fff;border:1px solid var(--frame);overflow:hidden}
  .caption{position:absolute;font-size:16px;color:var(--ink)}
  .headline{position:absolute;font-weight:700;line-height:1.05;letter-spacing:-0.2px}
  .checklist{position:absolute;list-style:none}
  .checklist li{display:flex;align-items:flex-start;gap:6px;color:var(--ink)}
  .tick{flex:none}
  .brand-name{position:absolute;color:var(--navy);font-weight:400;white-space:nowrap}
  .cta{position:absolute;color:var(--cta-red);white-space:nowrap}
  .cta strong{font-weight:700}
  .gauge-photo{position:absolute}
  .corner-badge{position:absolute}

  /* 600 x 200 */
  .banner--wide{left:360px;top:96px;width:602px;height:202px}
  .banner--wide .headline{left:20px;top:16px;font-size:30px}
  .banner--wide .subline{position:absolute;left:22px;top:82px;font-size:16px}
  .banner--wide .checklist{top:112px;font-size:12.5px}
  .banner--wide .checklist li{margin-bottom:8px}
  .banner--wide .col-a{left:24px}
  .banner--wide .col-b{left:229px}
  .banner--wide .brand-name{left:17px;top:165px;font-size:13px}
  .banner--wide .cta{left:189px;top:165px;font-size:17px}
  .banner--wide .gauge-photo{left:412px;top:-6px;width:214px;height:214px;border-radius:50%;
    background:radial-gradient(circle at 50% 46%,var(--gauge-face) 0%,var(--gauge-face) 52%,#9aa09b 58%,var(--gauge-dark) 64%,#3e4347 100%)}
  .banner--wide .corner-badge{right:0;top:0}

  /* 600 x 100 */
  .banner--strip{left:360px;top:427px;width:602px;height:102px}
  .banner--strip .headline{left:98px;top:13px;font-size:22px}
  .banner--strip .checklist{top:40px;font-size:11px}
  .banner--strip .checklist li{margin-bottom:5px}
  .banner--strip .col-a{left:100px}
  .banner--strip .col-b{left:286px}
  .banner--strip .cta{left:98px;top:79px;font-size:14px}
  .banner--strip .brand-name{left:336px;top:77px;font-size:11px}
  .banner--strip .gauge-photo{left:478px;top:0;width:124px;height:102px;
    background:radial-gradient(circle at 78% 50%,var(--gauge-face) 0%,var(--gauge-face) 42%,#9aa09b 50%,var(--gauge-dark) 58%,#5c6166 80%,#dfe2df 100%)}
  .banner--strip .corner-badge{left:0;top:0}

  /* 120 x 500 */
  .banner--tower{left:1037px;top:95px;width:122px;height:502px}
  .banner--tower .brand-name{left:0;width:120px;top:40px;text-align:center;font-size:11px;line-height:1.3;white-space:normal}
  .banner--tower .headline{left:8px;top:90px;font-size:18px;line-height:1.12}
  .banner--tower .checklist{left:8px;top:165px;width:104px;font-size:9.5px;line-height:1.25}
  .banner--tower .checklist li{margin-bottom:6px}
  .trust-box{position:absolute;left:6px;top:312px;width:109px;height:50px;background:var(--brand-red);color:#fff;text-align:center}
  .trust-box .est{display:flex;align-items:center;justify-content:center;gap:5px;font-size:9px;margin-top:4px}
  .trust-box .est::before,.trust-box .est::after{content:"";display:block;width:22px;height:1px;background:#fff}
  .trust-box .claim{font-size:10.5px;font-weight:700;font-style:italic;line-height:1.1;margin-top:3px}
  .banner--tower .gauge-photo{left:0;top:375px;width:120px;height:127px;
    background:radial-gradient(circle at 50% 45%,var(--gauge-face) 0%,var(--gauge-face) 38%,#9aa09b 46%,var(--gauge-dark) 54%,#5c6166 75%,#cfd2cf 100%)}
  .banner--tower .cta{left:7px;top:450px;width:107px;height:42px;background:#fff;text-align:center;font-size:13px;line-height:1.2;padding-top:6px}
</style>
</head>
<body>
<svg width="0" height="0" style="position:absolute" aria-hidden="true">
  <defs>
    <symbol id="tick-box" viewBox="0 0 14 14">
      <rect x="1" y="2" width="11" height="11" fill="none" stroke="#222" stroke-width="1.3"/>
      <path d="M3.5 7.5 L6 10.5 L13 2" fill="none" stroke="#d0174a" stroke-width="1.8"/>
    </symbol>
  </defs>
</svg>

<main class="canvas">
  <div class="stage">

    <div class="submission-notes">
      <p><strong>Design Submission</strong></p>
      <p>Crestline Valve banners</p>
      <p>01 Mar, 2018</p>
      <p>(additonal request)</p>
    </div>

    <section class="banner banner--wide" aria-label="Banner 600 by 200">
      <div class="gauge-photo" role="img" aria-label="Close-up photo of a differential pressure test gauge"></div>
      <svg class="corner-badge" width="110" height="92" viewBox="0 0 110 92" aria-hidden="true">
        <polygon points="0,0 110,0 110,92" fill="var(--brand-red)"/>
        <g transform="translate(70,30) rotate(40)" fill="#fff" text-anchor="middle" font-family="Arimo,Arial,sans-serif">
          <text x="0" y="-8" font-size="10">Est. 1976</text>
          <text x="2" y="6" font-size="12" font-weight="700" font-style="italic">Trusted for</text>
          <text x="2" y="19" font-size="12" font-weight="700" font-style="italic">over 40 years</text>
        </g>
      </svg>
      <h2 class="headline">We’re Your<br>One-Stop Shop</h2>
      <p class="subline">Easy, quick &amp; affordable</p>
      <ul class="checklist col-a">
        <li><svg class="tick" width="14" height="14"><use href="#tick-box"/></svg>Backflow preventer repair parts</li>
        <li><svg class="tick" width="14" height="14"><use href="#tick-box"/></svg>Test gauge calibration</li>
      </ul>
      <ul class="checklist col-b">
        <li><svg class="tick" width="14" height="14"><use href="#tick-box"/></svg>Accessories &amp; enclosures</li>
        <li><svg class="tick" width="14" height="14"><use href="#tick-box"/></svg>Nationwide delivery</li>
      </ul>
      <p class="brand-name">Crestline Valve Supply</p>
      <p class="cta"><strong>BOOK TODAY</strong> (800) 555 0142</p>
    </section>
    <p class="caption" style="left:360px;top:306px">Banner 600 x 200</p>

    <section class="banner banner--strip" aria-label="Banner 600 by 100">
      <div class="gauge-photo" role="img" aria-label="Close-up photo of a differential pressure test gauge"></div>
      <svg class="corner-badge" width="98" height="100" viewBox="0 0 98 100" aria-hidden="true">
        <polygon points="0,0 98,0 0,100" fill="var(--brand-red)"/>
        <g transform="translate(32,34) rotate(-45)" fill="#fff" text-anchor="middle" font-family="Arimo,Arial,sans-serif">
          <text x="0" y="-10" font-size="9.5">Est. 1976</text>
          <text x="0" y="4" font-size="11.5" font-weight="700" font-style="italic">Trusted for</text>
          <text x="0" y="17" font-size="11.5" font-weight="700" font-style="italic">over 40 years</text>
        </g>
      </svg>
      <h2 class="headline">We’re Your One-Stop Shop</h2>
      <ul class="checklist col-a">
        <li><svg class="tick" width="13" height="13"><use href="#tick-box"/></svg>Backflow preventer repair parts</li>
        <li><svg class="tick" width="13" height="13"><use href="#tick-box"/></svg>Test gauge calibration</li>
      </ul>
      <ul class="checklist col-b">
        <li><svg class="tick" width="13" height="13"><use href="#tick-box"/></svg>Accessories &amp; enclosures</li>
        <li><svg class="tick" width="13" height="13"><use href="#tick-box"/></svg>Nationwide delivery</li>
      </ul>
      <p class="cta"><strong>BOOK TODAY</strong> (800) 555 0142</p>
      <p class="brand-name">Crestline Valve Supply</p>
    </section>
    <p class="caption" style="left:360px;top:542px">Banner 600 x 100</p>

    <section class="banner banner--tower" aria-label="Banner 120 by 500">
      <p class="brand-name">Crestline<br>Valve Supply</p>
      <h2 class="headline">We’re Your<br>One-Stop<br>Shop</h2>
      <ul class="checklist">
        <li><svg class="tick" width="12" height="12"><use href="#tick-box"/></svg>Backflow preventer repair parts</li>
        <li><svg class="tick" width="12" height="12"><use href="#tick-box"/></svg>Accessories</li>
        <li><svg class="tick" width="12" height="12"><use href="#tick-box"/></svg>Enclosures</li>
        <li><svg class="tick" width="12" height="12"><use href="#tick-box"/></svg>Test gauge<br>calibration</li>
        <li><svg class="tick" width="12" height="12"><use href="#tick-box"/></svg>Nationwide delivery</li>
        <li><svg class="tick" width="12" height="12"><use href="#tick-box"/></svg>No minimum orders</li>
      </ul>
      <div class="trust-box">
        <p class="est">Est. 1976</p>
        <p class="claim">Trusted for<br>over 40 years</p>
      </div>
      <div class="gauge-photo" role="img" aria-label="Close-up photo of a differential pressure test gauge"></div>
      <p class="cta"><strong>BOOK TODAY</strong><br>(800) 555 0142</p>
    </section>
    <p class="caption" style="left:1036px;top:610px">Banner 120 x 500</p>

  </div>
</main>
</body>
</html>
```